Agribusiness Insurance

I would like postcard designed to attract farmers and agribusiness owners to my insurance consulting services. My business model is being a Trusted Advisor through identifying exposures, developing strategies, implementing programs and then monitoring our designed plan. I am knowledge representative (13YRs ag insurance), Represent 15 Farm + Carriers (favorable pricing/competitive multiple options) Specialized in Confinements, Cattle Farms, and Grain Producers. No Membership Fees Necessary

Many Insurance Producers in my area are nearing retirement I am 33 and am looking to promote this..

Target Market(s)

Farmers and Agribusiness Owners

Industry/Entity Type

Agribusiness

Requirements
Must have

• Owen Telfer
Phone: Cell 555 207 6413
Email: otelfer@ridgeplainagency.example

```html
<!DOCTYPE html>
<html lang="en">
<head>
<meta charset="utf-8">
<title>Agribusiness Insurance Postcard</title>
<link rel="stylesheet" href="https://fonts.googleapis.com/css2?family=Oswald:wght@700&family=Roboto+Condensed:ital,wght@0,700;1,700&display=swap">
<style>
  :root {
    --paper: #ffffff;
    --sky-top: #2f5877;
    --sky-mid: #7fb3cf;
    --sky-low: #b9dbe9;
    --hill: #b98a58;
    --hill-dark: #8f6338;
    --field: #5f9a3a;
    --field-light: #86c04e;
    --headline: #f07f1e;
    --headline-shadow: #3a2412;
    --band-red: #c4202f;
    --band-orange: #ee7d1f;
    --band-orange-light: #f49b2c;
    --ink: #1c1c1c;
    --white: #ffffff;
    --frame-photo: #8a8683;
    --footer-bar: #111111;
  }
  * { margin: 0; padding: 0; box-sizing: border-box; }
  html, body { width: 1200px; height: 930px; overflow: hidden; background: var(--paper); }
  .postcard { position: relative; width: 1200px; height: 930px; background: var(--paper); }

  .scenery {
    position: absolute; left: 30px; top: 30px; width: 1140px; height: 848px;
    background: linear-gradient(180deg,
      var(--sky-top) 0%, var(--sky-mid) 24%, var(--sky-low) 38%,
      var(--hill) 40%, var(--hill-dark) 48%,
      var(--field) 50%, var(--field-light) 70%, var(--field) 100%);
  }

  .headline {
    position: absolute; left: 30px; top: 84px; width: 1140px;
    text-align: center;
    font-family: "Oswald", "Arial Narrow", sans-serif;
    font-weight: 700; font-size: 74px; line-height: 1; letter-spacing: 1px;
    color: var(--headline);
    text-shadow: 3px 3px 0 var(--headline-shadow);
  }

  .waves { position: absolute; left: 0; top: 0; width: 1200px; height: 930px; }

  .benefits {
    position: absolute; left: 750px; top: 428px; list-style: none;
    font-family: "Roboto Condensed", "Arial Narrow", sans-serif;
    font-style: italic; font-weight: 700; font-size: 25px; line-height: 44.6px;
    color: var(--white);
    text-shadow: 2px 2px 2px rgba(0,0,0,.75);
  }
  .benefits li { display: flex; align-items: center; }
  .benefits .tick { width: 22px; height: 20px; margin-right: 14px; flex: none; }

  .agent-photo {
    position: absolute; left: 75px; top: 613px; width: 184px; height: 246px;
    background: var(--white); padding: 6px;
    box-shadow: 2px 3px 6px rgba(0,0,0,.4);
  }
  .agent-photo .portrait {
    width: 100%; height: 100%;
    background: linear-gradient(180deg, #9a9692 0%, var(--frame-photo) 60%, #2a2a2a 100%);
  }

  .contact {
    position: absolute; left: 287px; top: 762px;
    font-family: "Roboto Condensed", "Arial Narrow", sans-serif;
    font-weight: 700; color: var(--ink);
  }
  .contact .agent-name { font-size: 33px; line-height: 38px; text-transform: uppercase; }
  .contact .line { font-size: 22px; line-height: 32px; }

  .footer-bar { position: absolute; left: 30px; top: 878px; width: 1140px; height: 20px; background: var(--footer-bar); }
</style>
</head>
<body>
<main class="postcard">
  <div class="scenery" role="img" aria-label="Photograph of rows of green crops stretching toward dry brown hills under a clear blue sky"></div>

  <h1 class="headline">INSURING YOUR FUTURE… TODAY</h1>

  <svg class="waves" viewBox="0 0 1200 930" aria-hidden="true">
    <defs>
      <linearGradient id="orangeFill" x1="0" y1="0" x2="1" y2="0">
        <stop offset="0" stop-color="var(--band-orange)"/>
        <stop offset="1" stop-color="var(--band-orange-light)"/>
      </linearGradient>
    </defs>
    <path fill="var(--band-red)" d="M30,585 C250,548 460,578 640,660 C820,742 1000,792 1170,768 L1170,792 C1000,812 800,772 620,682 C450,602 250,572 30,602 Z"/>
    <path fill="url(#orangeFill)" d="M30,602 C250,572 450,602 620,682 C800,772 1000,812 1170,792 L1170,878 L30,878 Z"/>
    <path fill="none" stroke="var(--band-red)" stroke-width="6" d="M490,652 C700,700 950,735 1170,740"/>
    <path fill="var(--band-red)" d="M620,682 C760,750 880,800 960,878 L900,878 C830,810 730,760 620,700 Z" opacity="0.85"/>
  </svg>

  <ul class="benefits">
    <li><svg class="tick" viewBox="0 0 22 20"><path d="M2,11 L8,17 L20,2" fill="none" stroke="#fff" stroke-width="3"/></svg>Represent 15 Farm + Carriers</li>
    <li><svg class="tick" viewBox="0 0 22 20"><path d="M2,11 L8,17 L20,2" fill="none" stroke="#fff" stroke-width="3"/></svg>favorable pricing</li>
    <li><svg class="tick" viewBox="0 0 22 20"><path d="M2,11 L8,17 L20,2" fill="none" stroke="#fff" stroke-width="3"/></svg>competitive multiple options</li>
    <li><svg class="tick" viewBox="0 0 22 20"><path d="M2,11 L8,17 L20,2" fill="none" stroke="#fff" stroke-width="3"/></svg>Specialized in Confinements</li>
    <li><svg class="tick" viewBox="0 0 22 20"><path d="M2,11 L8,17 L20,2" fill="none" stroke="#fff" stroke-width="3"/></svg>Grain Producers</li>
    <li><svg class="tick" viewBox="0 0 22 20"><path d="M2,11 L8,17 L20,2" fill="none" stroke="#fff" stroke-width="3"/></svg>Cattle Farms</li>
    <li><svg class="tick" viewBox="0 0 22 20"><path d="M2,11 L8,17 L20,2" fill="none" stroke="#fff" stroke-width="3"/></svg>No Membership Fees</li>
  </ul>

  <figure class="agent-photo">
    <div class="portrait" role="img" aria-label="Head-and-shoulders portrait of the agent in a dark suit and red shirt"></div>
  </figure>

  <address class="contact">
    <div class="agent-name">Owen Telfer</div>
    <div class="line">Phone: Cell 555 207 6413</div>
    <div class="line">Email: otelfer@ridgeplainagency.example</div>
  </address>

  <div class="footer-bar"></div>
</main>
</body>
</html>
```